Cover for Every door Opens Where Every Door Opens

Book Cover Request
Format: Print and electronic (Quillmart)
Book Title: Every Door Opens Where Every Door Opens: Practical Roadmap for Courage and Progress
Author: R.K. Vantreel
Description: This self-help book, written by me, a self-proclaimed nobody, is filled with actionable insights and proven strategies that can help anyone. It combines humor with a serious undertone to deliver practical advice without the typical "self-helpy" vibe.
Catchphrase for the Cover: "Go from Oh Shit to Crushing It!" (or something similar)
Style: I want the cover to reflect my personality—funny, yet serious when needed. I'm open to suggestions and would love to see a design that captures the essence of the book without being too typical of the self-help genre.
Additional Information: I've attached a rough draft of the Quillmart description for more context.
Thank you for your help!
Target Market(s)
Anyone. but id say over 25
Requirements
Nice to have
- Honestly im really at a loss. Im hoping the description will help guide you. I gues i would like it to satand out of course. Be diffrent....but i know how crazy that sounds because everyone wants that. Just give me soem ideas!

```html
<!DOCTYPE html>
<html lang="en">
<head>
<meta charset="utf-8">
<title>Every Door Opens Where Every Door Opens — Cover</title>
<link href="https://fonts.googleapis.com/css2?family=Allura&family=Bebas+Neue&family=Poppins:wght@600;700&display=swap" rel="stylesheet">
<style>
  :root {
    --page: #ffffff;
    --sun: #ffdc35;
    --amber: #fcb328;
    --orange: #fd981c;
    --ink: #262626;
    --paper: #f0f1f5;
    --script: #f6a11c;
  }
  html, body {
    margin: 0;
    width: 1200px;
    height: 1200px;
    overflow: hidden;
    background: var(--page);
  }
  .book-cover {
    position: absolute;
    left: 233px;
    top: 50px;
    width: 733px;
    height: 1099px;
    display: block;
  }
  .author { font-family: "Poppins", sans-serif; font-weight: 600; fill: var(--paper); }
  .title-line { font-family: "Poppins", sans-serif; font-weight: 700; fill: var(--paper); }
  .title-big { font-family: "Bebas Neue", sans-serif; }
  .title-big--dark { fill: var(--ink); }
  .title-big--orange { fill: var(--amber); }
  .title-joiner { font-family: "Allura", cursive; fill: var(--script); }
  .subtitle-top { font-family: "Poppins", sans-serif; font-weight: 600; fill: var(--paper); }
  .subtitle-main { font-family: "Poppins", sans-serif; font-weight: 700; fill: var(--ink); }
  .subtitle-and { fill: var(--paper); font-weight: 600; }
</style>
</head>
<body>
<svg class="book-cover" viewBox="376 81 1180 1769" xmlns="http://www.w3.org/2000/svg" aria-label="Book cover: Every Door Opens Where Every Door Opens by R.K. Vantreel">
  <defs>
    <radialGradient id="cover-glow" cx="1040" cy="100" r="1400" gradientUnits="userSpaceOnUse">
      <stop offset="0" stop-color="var(--sun)"/>
      <stop offset="0.55" stop-color="var(--amber)"/>
      <stop offset="1" stop-color="var(--orange)"/>
    </radialGradient>
  </defs>

  <rect class="cover-base" x="376" y="81" width="1180" height="1769" fill="url(#cover-glow)"/>

  <!-- torn band: paper edge then dark core -->
  <path class="torn-edge" fill="var(--paper)" d="M376 712 L390 705 L410 712 L430 708 L450 716 L470 728 L490 730 L510 760 L530 790 L550 815 L580 818 L610 822 L650 815 L700 820 L760 818 L820 812 L860 790 L890 776 L915 780 L930 792 L950 808 L975 835 L1000 842 L1040 840 L1080 834 L1130 838 L1180 845 L1240 848 L1300 848 L1360 852 L1400 858 L1430 862 L1470 870 L1510 880 L1556 885 L1556 1605 L1530 1595 L1500 1580 L1470 1560 L1440 1528 L1420 1515 L1380 1520 L1330 1518 L1290 1522 L1240 1520 L1190 1515 L1150 1512 L1130 1530 L1110 1560 L1085 1590 L1060 1598 L1030 1570 L1010 1540 L990 1520 L960 1508 L920 1515 L880 1525 L830 1528 L780 1526 L730 1530 L680 1535 L620 1532 L560 1520 L520 1515 L480 1518 L440 1510 L420 1512 L400 1525 L376 1545 Z"/>
  <path class="torn-band" fill="var(--ink)" d="M376 730 L400 725 L430 726 L460 740 L480 760 L505 770 L520 800 L545 840 L580 836 L620 832 L660 830 L720 835 L780 836 L830 818 L870 800 L905 798 L930 815 L955 840 L980 865 L1010 876 L1050 870 L1090 858 L1140 855 L1200 860 L1260 858 L1310 866 L1360 885 L1400 888 L1440 878 L1480 890 L1520 905 L1556 912 L1556 1590 L1520 1580 L1490 1560 L1460 1535 L1435 1505 L1400 1505 L1340 1500 L1280 1498 L1220 1500 L1170 1500 L1140 1525 L1115 1555 L1075 1575 L1045 1555 L1020 1525 L995 1500 L960 1490 L920 1495 L880 1505 L830 1510 L780 1505 L730 1508 L680 1512 L620 1510 L565 1498 L520 1498 L470 1495 L430 1498 L400 1510 L376 1530 Z"/>

  <text class="author" x="607" y="197" font-size="80" textLength="733" lengthAdjust="spacing">R.K. VANTREEL</text>

  <text class="title-line" x="562" y="406" font-size="172" textLength="823" lengthAdjust="spacingAndGlyphs">EVERY DOOR</text>
  <text class="title-big title-big--dark" x="470" y="712" font-size="378" textLength="1008" lengthAdjust="spacingAndGlyphs">OPENS</text>

  <text class="title-line" x="562" y="1172" font-size="172" textLength="823" lengthAdjust="spacingAndGlyphs">EVERY DOOR</text>
  <text class="title-joiner" x="650" y="1020" font-size="300" textLength="575" lengthAdjust="spacingAndGlyphs">Where</text>
  <text class="title-big title-big--orange" x="470" y="1478" font-size="378" textLength="1008" lengthAdjust="spacingAndGlyphs">OPENS</text>

  <text class="subtitle-top" x="577" y="1685" font-size="66" textLength="785" lengthAdjust="spacingAndGlyphs">PRACTICAL ROADMAP FOR</text>
  <text class="subtitle-main" x="432" y="1779" font-size="98" textLength="1048" lengthAdjust="spacingAndGlyphs">COURAGE <tspan class="subtitle-and" font-size="58">AND</tspan> PROGRESS</text>
</svg>
</body>
</html>
```